PLM - Business Card Design Project

We need a business card based on our logo
Updates

Hi I just upload logo file in AI format Thanks and regards

Target Market(s)

Bank, Big companies, Business owners

Industry/Entity Type

Business

Font styles to use
Sans Serif

```html
<!DOCTYPE html>
<html lang="en">
<head>
<meta charset="utf-8">
<title>PLM Business Card</title>
<link rel="stylesheet" href="https://fonts.googleapis.com/css2?family=Open+Sans:wght@400;600;700&display=swap">
<style>
  :root {
    --backdrop: #b4b9b8;
    --card-white: #ffffff;
    --navy: #1b2a4c;
    --navy-dark: #131d30;
    --slate: #87948f;
    --muted: #7d8580;
    --contact-text: #ffffff;
    --icon: #c9cfd3;
  }
  * { margin: 0; padding: 0; box-sizing: border-box; }
  html, body {
    width: 1200px;
    height: 900px;
    overflow: hidden;
    background: var(--backdrop);
    font-family: "Open Sans", sans-serif;
  }
  .business-card {
    position: absolute;
    left: 160px;
    top: 195px;
    width: 880px;
    height: 510px;
    border-radius: 34px;
    overflow: hidden;
    background: var(--card-white);
  }
  .brand-block {
    position: absolute;
    left: 56px;
    top: 34px;
  }
  .brand-name {
    display: block;
    font-size: 150px;
    line-height: 1;
    font-weight: 400;
    letter-spacing: 4px;
    color: var(--navy);
  }
  .company-name {
    margin-top: 6px;
    font-size: 27px;
    font-weight: 400;
    color: var(--navy);
    white-space: nowrap;
  }
  .company-tagline {
    margin-top: 2px;
    padding-left: 62px;
    font-size: 12.5px;
    color: var(--muted);
    letter-spacing: 0.3px;
  }
  .person {
    position: absolute;
    right: 38px;
    top: 58px;
    text-align: right;
  }
  .person-name {
    font-size: 26px;
    font-weight: 600;
    color: var(--navy);
  }
  .person-title {
    font-size: 16px;
    color: var(--muted);
  }
  .accent-band {
    position: absolute;
    left: 0;
    top: 266px;
    width: 100%;
    height: 20px;
    background: var(--slate);
  }
  .contact-panel {
    position: absolute;
    left: 0;
    top: 286px;
    width: 100%;
    height: 224px;
    background: var(--navy-dark);
  }
  .contact-list {
    list-style: none;
    position: absolute;
    left: 56px;
    top: 28px;
  }
  .contact-item {
    display: flex;
    align-items: center;
    height: 33px;
    font-size: 24px;
    color: var(--contact-text);
  }
  .contact-item.continued { padding-left: 40px; }
  .contact-icon {
    width: 26px;
    height: 26px;
    margin-right: 14px;
    flex: none;
    fill: var(--icon);
    stroke: none;
  }
</style>
</head>
<body>
  <div class="business-card">
    <div class="brand-block">
      <span class="brand-name">PLM</span>
      <p class="company-name">Cabinet Perrin Lemaire &amp; Martin</p>
      <p class="company-tagline">Expertise-comptable • Audit • Conseil</p>
    </div>

    <div class="person">
      <p class="person-name">Julien Morel</p>
      <p class="person-title">Manager</p>
    </div>

    <div class="accent-band"></div>

    <div class="contact-panel">
      <ul class="contact-list">
        <li class="contact-item">
          <svg class="contact-icon" viewBox="0 0 24 24" aria-hidden="true">
            <rect x="6" y="2" width="12" height="20" rx="2"/>
            <rect x="8" y="4.5" width="8" height="6" fill="#131d30"/>
            <rect x="8" y="12.5" width="2" height="2" fill="#131d30"/>
            <rect x="11" y="12.5" width="2" height="2" fill="#131d30"/>
            <rect x="14" y="12.5" width="2" height="2" fill="#131d30"/>
            <rect x="8" y="16" width="2" height="2" fill="#131d30"/>
            <rect x="11" y="16" width="2" height="2" fill="#131d30"/>
            <rect x="14" y="16" width="2" height="2" fill="#131d30"/>
          </svg>
          154 555 0182
        </li>
        <li class="contact-item">
          <svg class="contact-icon" viewBox="0 0 24 24" aria-hidden="true">
            <path d="M6.6 10.8a15.1 15.1 0 0 0 6.6 6.6l2.2-2.2c.3-.3.7-.4 1-.2 1.1.4 2.3.6 3.6.6.6 0 1 .4 1 1V20c0 .6-.4 1-1 1A17 17 0 0 1 3 4c0-.6.4-1 1-1h3.5c.6 0 1 .4 1 1 0 1.3.2 2.5.6 3.6.1.3 0 .7-.2 1z"/>
          </svg>
          154 555 0147
        </li>
        <li class="contact-item">
          <svg class="contact-icon" viewBox="0 0 24 24" aria-hidden="true">
            <path d="M12 2a10 10 0 1 0 0 20 10 10 0 0 0 0-20zm6.9 6h-2.9a15.6 15.6 0 0 0-1.4-3.6A8 8 0 0 1 18.9 8zM12 4c.8 1.2 1.5 2.5 1.9 4h-3.8c.4-1.5 1.1-2.8 1.9-4zM4.3 14a8.2 8.2 0 0 1 0-4h3.4a16.5 16.5 0 0 0 0 4zm.8 2h2.9c.3 1.3.8 2.5 1.4 3.6A8 8 0 0 1 5.1 16zM8 8H5.1a8 8 0 0 1 4.3-3.6C8.8 5.5 8.3 6.7 8 8zm4 12c-.8-1.2-1.5-2.5-1.9-4h3.8c-.4 1.5-1.1 2.8-1.9 4zm2.3-6H9.7a14.7 14.7 0 0 1 0-4h4.6a14.7 14.7 0 0 1 0 4zm.3 5.6c.6-1.1 1.1-2.3 1.4-3.6h2.9a8 8 0 0 1-4.3 3.6zm1.7-5.6a16.5 16.5 0 0 0 0-4h3.4a8.2 8.2 0 0 1 0 4z"/>
          </svg>
          www.cabinetplm.com
        </li>
        <li class="contact-item">
          <svg class="contact-icon" viewBox="0 0 24 24" aria-hidden="true">
            <path d="M2 9l10-6 10 6v11H2z"/>
            <path d="M4 10l8 5 8-5" fill="none" stroke="#131d30" stroke-width="1.6"/>
          </svg>
          info@cabinetplm.com
        </li>
        <li class="contact-item">
          <svg class="contact-icon" viewBox="0 0 24 24" aria-hidden="true">
            <path d="M12 3 1.5 12.5h3V21h6v-5.5h3V21h6v-8.5h3z"/>
          </svg>
          Po Box: 418 Birchfield Rd.
        </li>
        <li class="contact-item continued">Millbrook, NJ. 08510</li>
      </ul>
    </div>
  </div>
</body>
</html>
```